Brightstone Roofing Business Card

This is my current business card. But I’d like to make some changes. Somewhere on the card I’d like to list some of the services we offer. Maybe on the back? But I’d still like to keep the red. White and black modern look.

-residential & commercial roofing
-Roof Repairs & Maintenance
-Storm Damage & Insurance Claims specialist
-Christmas Lights and permanent Christmas lights
Fencing. Windows. Gutters. Siding. Sheetrock, painting.

```html
<!DOCTYPE html>
<html lang="en">
<head>
<meta charset="utf-8">
<title>Brightstone Roofing Business Card</title>
<link href="https://fonts.googleapis.com/css2?family=Audiowide&family=Open+Sans:wght@400;600;700&display=swap" rel="stylesheet">
<style>
  :root {
    --bg: #d1d2d4;
    --white: #ffffff;
    --black: #000000;
    --red: #dc2026;
    --red-bright: #e3000f;
    --red-dark: #6e0e10;
    --ink: #1a1a1a;
  }
  * { margin: 0; padding: 0; box-sizing: border-box; }
  html, body { width: 1200px; height: 1200px; overflow: hidden; }
  body { background: var(--bg); position: relative; font-family: "Open Sans", sans-serif; }

  .card {
    position: absolute;
    width: 800px;
    height: 457px;
    border-radius: 19px;
    overflow: hidden;
    background: var(--white);
  }
  .card--front { left: 193px; top: 107px; }
  .card--back  { left: 207px; top: 635px; }

  .brand-mark {
    position: absolute;
    border-radius: 50%;
    background: var(--red-bright);
  }
  .brand-name {
    position: absolute;
    font-family: "Audiowide", sans-serif;
    font-weight: 400;
    color: var(--black);
    text-align: center;
    line-height: 1.1;
    letter-spacing: 1px;
  }

  /* front */
  .card--front .brand-mark { left: 315px; top: 61px; width: 170px; height: 170px; }
  .card--front .brand-name { left: 0; width: 800px; top: 252px; font-size: 40px; }
  .plaid-band { position: absolute; left: 0; top: 342px; width: 800px; height: 115px; }

  /* back */
  .card--back .brand-mark { left: 148px; top: 51px; width: 118px; height: 118px; }
  .card--back .brand-name { left: 0; width: 414px; top: 184px; font-size: 27px; }

  .services {
    position: absolute;
    left: 18px;
    top: 305px;
    font-size: 15px;
    line-height: 19.7px;
    color: var(--ink);
  }
  .services h3 { font-size: 15px; font-weight: 700; }
  .services li { list-style: none; }
  .services .indent { padding-left: 12px; }

  .contact-panel {
    position: absolute;
    left: 414px; top: 0;
    width: 386px; height: 457px;
    background: var(--black);
  }
  .red-tab {
    position: absolute;
    left: 387px;
    width: 55px;
    background: var(--red);
  }
  .red-tab--top { top: 0; height: 109px; border-radius: 0 0 12px 12px; }
  .red-tab--bottom { top: 223px; height: 234px; border-radius: 12px 12px 0 0; }

  .icon-box {
    position: absolute;
    left: 396px;
    width: 37px; height: 37px;
    border-radius: 8px;
    background: var(--black);
    display: flex; align-items: center; justify-content: center;
  }
  .icon-box svg { width: 24px; height: 24px; }

  .holder-name {
    position: absolute;
    left: 458px; top: 36px;
    font-family: "Audiowide", sans-serif;
    font-size: 31px;
    color: var(--white);
    letter-spacing: 1px;
  }
  .holder-name .first { color: var(--red); }
  .holder-role {
    position: absolute;
    left: 459px; top: 78px;
    font-size: 19px;
    font-weight: 600;
    color: var(--white);
    letter-spacing: 5px;
  }
  .contact-line {
    position: absolute;
    left: 458px;
    font-size: 24px;
    font-weight: 600;
    color: var(--white);
  }
  .contact-line--phone { top: 254px; letter-spacing: 3px; }
  .contact-line--web { top: 320px; }
  .contact-line--mail { top: 386px; }
</style>
</head>
<body>

<section class="card card--front">
  <div class="brand-mark"></div>
  <div class="brand-name">BRIGHTSTONE<br>ROOFING CO.</div>
  <svg class="plaid-band" viewBox="0 0 800 115" role="img" aria-label="Red and black tartan plaid band">
    <defs>
      <linearGradient id="plaidTone" x1="0" y1="0" x2="1" y2="0">
        <stop offset="0" stop-color="#8c1014"/>
        <stop offset="0.3" stop-color="#dc2026"/>
        <stop offset="0.7" stop-color="#c81b21"/>
        <stop offset="1" stop-color="#7a0f12"/>
      </linearGradient>
    </defs>
    <polygon points="0,0 123,0 158,62 643,62 677,0 800,0 800,115 0,115" fill="url(#plaidTone)"/>
  </svg>
</section>

<section class="card card--back">
  <div class="brand-mark"></div>
  <div class="brand-name">BRIGHTSTONE<br>ROOFING CO.</div>

  <div class="services">
    <h3>service:</h3>
    <ul>
      <li>- residential &amp; commercial roofing</li>
      <li>- Roof Repairs &amp; Maintenance</li>
      <li>- Storm Damage &amp; Insurance Claims specialist</li>
      <li>- Christmas Lights and permanent Christmas lights</li>
      <li class="indent">Fencing. Windows. Gutters. Siding. Sheetrock,</li>
      <li class="indent">painting.</li>
    </ul>
  </div>

  <div class="contact-panel"></div>
  <div class="red-tab red-tab--top"></div>
  <div class="red-tab red-tab--bottom"></div>

  <div class="icon-box" style="top:43px">
    <svg viewBox="0 0 24 24"><rect x="2" y="2" width="20" height="20" rx="4" fill="#fff"/><circle cx="12" cy="9" r="4" fill="#000"/><path d="M4 20c0-4 4-6 8-6s8 2 8 6z" fill="#000"/></svg>
  </div>
  <div class="holder-name"><span class="first">EVAN</span> MARSH</div>
  <div class="holder-role">OWNER</div>

  <div class="icon-box" style="top:252px">
    <svg viewBox="0 0 24 24"><path d="M6.6 2.5l3 3.3-1.8 2.4c1.2 2.7 3.3 4.8 6 6l2.4-1.8 3.3 3-1.8 3.4c-7.8-.6-13.7-6.5-14.4-14.4z" fill="#fff"/></svg>
  </div>
  <div class="contact-line contact-line--phone">555 - 214 - 3098</div>

  <div class="icon-box" style="top:318px">
    <svg viewBox="0 0 24 24"><rect x="1.5" y="4.5" width="21" height="15" rx="1.5" fill="none" stroke="#fff" stroke-width="1.8"/><path d="M2 5.5l10 8 10-8M2 19l7.5-7M22 19l-7.5-7" fill="none" stroke="#fff" stroke-width="1.6"/></svg>
  </div>
  <div class="contact-line contact-line--web">www.brightstoneroofing.co</div>

  <div class="icon-box" style="top:385px">
    <svg viewBox="0 0 24 24" fill="none" stroke="#fff" stroke-width="1.6"><circle cx="12" cy="12" r="10"/><ellipse cx="12" cy="12" rx="4.5" ry="10"/><path d="M2 12h20M4 6.5h16M4 17.5h16"/></svg>
  </div>
  <div class="contact-line contact-line--mail">Evan@brightstoneroofing.co</div>
</section>

</body>
</html>
```